Breakfast Cafe - The Coral Table

It is for my breakfast and lunch cafe with a hawaiian / beach theme. I am open 7 days a week from 7am to 2pm. We serve traditional American food such as omelettes, pancakes, burgers and sandwiches. I'll upload my old card and my new logo to be used. We have a lot of day to day regulars who eat there during the week, our t-shirts actually say 'Locals Only' on them. Hope this helps. Thanks.

Target Market(s)

anyone who has an appetite!

Industry/Entity Type

American Restaurant

Contact Information for Business Card

4815C Driftwood Shore Road
Long Beach, California
(562) 555-0187

Requirements
Must have
• Address and phone number easily readable.
Nice to have
• beach or tropical theme

```html
<!DOCTYPE html>
<html lang="en">
<head>
<meta charset="utf-8">
<title>The Coral Table – Business Card</title>
<link href="https://fonts.googleapis.com/css2?family=Oswald:wght@300;400;600&family=Saira+Condensed:wght@600&display=swap" rel="stylesheet">
<style>
  :root {
    --backdrop: #4e5a63;
    --paper: #ffffff;
    --wood-light: #b0611f;
    --wood-mid: #a2531a;
    --wood-dark: #8c4314;
    --wood-band: #85391a;
    --gold: #e8b828;
    --gold-soft: #c99a1e;
    --ink-light: #fff6e8;
    --ink-dark: #3a2010;
    --brand-blue: #4ab3d4;
    --brand-brown: #a85a1c;
    --emblem-orange: #f3a23c;
  }
  html, body {
    margin: 0;
    padding: 0;
    width: 1015px;
    height: 1200px;
    overflow: hidden;
    background: var(--backdrop);
  }
  .canvas {
    width: 1015px;
    height: 1200px;
    display: flex;
    align-items: center;
    justify-content: center;
  }
  .business-card {
    width: 640px;
    height: 1118px;
    display: block;
  }
  .info-text {
    font-family: "Oswald", sans-serif;
    font-weight: 300;
    fill: var(--ink-light);
  }
  .brand-name {
    font-family: "Oswald", sans-serif;
    font-weight: 600;
    fill: var(--brand-blue);
    letter-spacing: 1px;
  }
  .brand-place {
    font-family: "Oswald", sans-serif;
    font-weight: 600;
    fill: var(--brand-brown);
    letter-spacing: 4px;
  }
  .tagline {
    font-family: "Saira Condensed", sans-serif;
    font-weight: 600;
    fill: var(--ink-dark);
  }
  .gold-frame {
    fill: none;
    stroke: var(--gold);
    stroke-width: 1.6;
  }
  .gold-icon {
    fill: var(--gold);
  }
  .gold-icon-line {
    fill: none;
    stroke: var(--gold);
    stroke-width: 2.4;
    stroke-linecap: round;
  }
</style>
</head>
<body>
<main class="canvas">
  <svg class="business-card" viewBox="0 0 601 1050" xmlns="http://www.w3.org/2000/svg" aria-label="The Coral Table business card">
    <defs>
      <linearGradient id="wood" x1="0" y1="0" x2="1" y2="1">
        <stop offset="0" stop-color="var(--wood-light)"/>
        <stop offset="0.5" stop-color="var(--wood-mid)"/>
        <stop offset="1" stop-color="var(--wood-dark)"/>
      </linearGradient>
      <clipPath id="card-clip"><rect width="601" height="1050"/></clipPath>
    </defs>

    <g clip-path="url(#card-clip)">
      <!-- wood surface -->
      <rect class="wood-surface" width="601" height="1050" fill="url(#wood)" role="img" aria-label="Warm wood grain surface"/>

      <!-- header arc -->
      <circle class="header-band" cx="300.5" cy="104" r="385" fill="var(--wood-band)"/>
      <path class="header-paper" d="M0,0 H601 V293 A355,355 0 0 1 0,293 Z" fill="var(--paper)"/>
    </g>

    <!-- brand block -->
    <g class="brand">
      <circle class="brand-emblem" cx="300.5" cy="193" r="138" fill="var(--emblem-orange)"/>
      <text class="brand-name" x="300.5" y="345" text-anchor="middle" font-size="46">The Coral Table</text>
      <text class="brand-place" x="300.5" y="381" text-anchor="middle" font-size="15">LONG BEACH, CA</text>
    </g>

    <!-- hours -->
    <g class="info hours">
      <path class="gold-frame" d="M282,527 H119 Q111,527 111,535 V586 Q111,594 119,594 H481 Q489,594 489,586 V535 Q489,527 481,527 H318"/>
      <g class="icon utensils">
        <line class="gold-icon-line" x1="287" y1="536" x2="312" y2="510"/>
        <line class="gold-icon-line" x1="313" y1="536" x2="290" y2="513"/>
        <circle class="gold-icon" cx="289" cy="512" r="5"/>
        <path class="gold-icon-line" d="M308,506 L316,514 M312,504 L318,510"/>
      </g>
      <text class="info-text" x="300" y="573" text-anchor="middle" font-size="30">Breakfast &amp; Lunch 7am-2pm Daily</text>
    </g>

    <!-- address -->
    <g class="info address">
      <path class="gold-frame" d="M285,639 H119 Q111,639 111,647 V748 Q111,756 119,756 H481 Q489,756 489,748 V647 Q489,639 481,639 H315"/>
      <path class="gold-icon" d="M300,652 C292,641 287,635 287,628 A13,13 0 0 1 313,628 C313,635 308,641 300,652 Z M300,623 A5,5 0 1 0 300.01,623 Z" fill-rule="evenodd"/>
      <text class="info-text" x="300" y="687" text-anchor="middle" font-size="29" letter-spacing="1">4815-C Driftwood Shore Road</text>
      <text class="info-text" x="300" y="734" text-anchor="middle" font-size="29" letter-spacing="1">Long Beach, California 90803</text>
    </g>

    <!-- phone -->
    <g class="info phone">
      <path class="gold-frame" d="M287,794 H205 Q197,794 197,802 V854 Q197,862 205,862 H395 Q403,862 403,854 V802 Q403,794 395,794 H313"/>
      <path class="gold-icon" d="M291,783 Q289,788 293,794 Q299,802 306,804 Q311,805 313,802 L309,797 Q306,799 303,797 Q298,793 296,788 Q295,785 297,784 Z"/>
      <path class="gold-icon-line" d="M303,782 A8,8 0 0 1 309,789 M304,776 A14,14 0 0 1 315,787" stroke-width="1.6"/>
      <text class="info-text" x="300" y="841" text-anchor="middle" font-size="31">562-555-0187</text>
    </g>

    <!-- footer -->
    <line class="footer-rule" x1="0" y1="912" x2="601" y2="912" stroke="var(--gold-soft)" stroke-width="1.5"/>
    <text class="tagline" x="300" y="990" text-anchor="middle" font-size="31">family owned &amp; operated!</text>
  </svg>
</main>
</body>
</html>
```